Real Estate Entrepreneur needs a business card

I am a real estate entrepreneur, I buy houses for investment purposes, I act as a real estate agent representing buyers and sellers in residential home transactions, I am a contractor that does a wide range of home repairs and construction. I'd like a design that can stick with me through the years as my business grows and morphs to fit any niche I decide to pursue as markets change.

Target Market(s)

Anyone with interest that may be related to real estate.

Industry/Entity Type

Real Estate

Contact Information for Business Card

A card that stands out and doesn't put me in any one box. My business will evolve over time and I need a card that can stay relevant.

Colors

Designer to choose colors to be used in the design.

Requirements
Must have
• Character
Nice to have
• I'm open
Should not have
• Cliche houses and hammers

```html
<!DOCTYPE html>
<html lang="en">
<head>
<meta charset="utf-8">
<title>Nash Vale – Business Cards</title>
<link rel="stylesheet" href="https://fonts.googleapis.com/css2?family=Montserrat:wght@300;400&family=Open+Sans:wght@400&display=swap">
<style>
  :root {
    --backdrop: #eaddd4;
    --card-top: #262b33;
    --card-bottom: #0f1620;
    --ink-light: #e4edf5;
    --ink-soft: #c9d3dc;
    --rule: #e4edf5;
  }
  * { margin: 0; padding: 0; box-sizing: border-box; }
  html, body {
    width: 1200px;
    height: 800px;
    overflow: hidden;
    background: var(--backdrop);
  }
  .canvas {
    position: relative;
    width: 1200px;
    height: 800px;
    display: flex;
    align-items: center;
    justify-content: center;
    gap: 40px;
  }
  .card {
    position: relative;
    width: 520px;
    height: 300px;
    background: linear-gradient(160deg, var(--card-top) 0%, var(--card-bottom) 100%);
    box-shadow: 0 10px 28px rgba(60, 40, 30, 0.25);
    color: var(--ink-light);
  }

  /* Letter-grid card */
  .letter-grid {
    position: absolute;
    left: 56px;
    top: 46px;
    font-family: "Montserrat", sans-serif;
    font-weight: 300;
    font-size: 58px;
    line-height: 70px;
    letter-spacing: 0.42em;
    color: var(--ink-light);
  }
  .letter-grid span { display: block; }
  .signature {
    position: absolute;
    right: 46px;
    bottom: 40px;
    font-family: "Open Sans", sans-serif;
    font-size: 14px;
    letter-spacing: 0.2em;
    color: var(--ink-soft);
    padding-bottom: 6px;
    border-bottom: 2px solid var(--rule);
  }

  /* Monogram card */
  .monogram {
    position: absolute;
    left: 0;
    right: 0;
    top: 46px;
    text-align: center;
    font-family: "Montserrat", sans-serif;
    font-weight: 300;
    font-size: 92px;
    letter-spacing: 0.04em;
    color: var(--ink-light);
  }
  .identity {
    position: absolute;
    left: 50%;
    top: 184px;
    transform: translateX(-50%);
    width: 250px;
    text-align: center;
  }
  .identity__name {
    font-family: "Open Sans", sans-serif;
    font-size: 19px;
    letter-spacing: 0.22em;
    color: var(--ink-light);
  }
  .identity__rule {
    height: 2px;
    margin: 8px 0 10px;
    background: var(--rule);
  }
  .identity__role {
    font-family: "Open Sans", sans-serif;
    font-size: 10px;
    letter-spacing: 0.42em;
    color: var(--ink-soft);
  }
</style>
</head>
<body>
  <main class="canvas">
    <section class="card card--letters" aria-label="Business card, letter side">
      <div class="letter-grid">
        <span>N ALE</span>
        <span>VALE</span>
        <span>VASH</span>
      </div>
      <p class="signature">Nash Vale</p>
    </section>

    <section class="card card--monogram" aria-label="Business card, monogram side">
      <p class="monogram">NV</p>
      <div class="identity">
        <p class="identity__name">NASH VALE</p>
        <div class="identity__rule"></div>
        <p class="identity__role">REAL ESTATE AGENT</p>
      </div>
    </section>
  </main>
</body>
</html>
```